New Website for novelty yarn producer

We need a new website for our company, Tarvek. We make highly tailored yarns for weavers worldwide. This year marks our 40th anniversary and we want to evolve our image and identity.

Our temporary website can be found at:
www.tarvekyarns.com

Our only concern in that throughout the website the protagonist must be our client, we make their creations possible and are highly adaptable both during the ideation process of the yarn as well as in the production. This is at the core of the way we do business and is summarised within the concept of FPM (Fluid Partner Method).

Industry/Entity Type

Textile

Number of Pages Required

1 page

Colors
9bcb3c

Requirements
Must have
• Fluid Partner Method (FPM) - can be found on or current website www.tarvekyarns.com

```html
<!DOCTYPE html>
<html lang="en">
<head>
<meta charset="utf-8">
<title>Tarvek – Tailored Weaving Solutions</title>
<link rel="stylesheet" href="https://fonts.googleapis.com/css2?family=Ubuntu:wght@300;400;500;700&display=swap">
<style>
:root{
  --green:#8cc21f;
  --green-dark:#76ab0a;
  --ink:#2a2a2a;
  --text:#3a3a3a;
  --muted:#555;
  --white:#fff;
  --footer:#2b2b2b;
  --line:#e4e4e4;
}
*{box-sizing:border-box;margin:0;padding:0}
html,body{width:1200px;height:3321px;overflow:hidden;background:var(--white)}
body{position:relative;font-family:"Ubuntu",sans-serif;color:var(--text)}
.abs{position:absolute}

/* nav */
.site-header{top:0;left:0;width:1200px;height:84px;background:var(--white)}
.brand{left:93px;top:16px;font-size:40px;font-weight:500;color:var(--ink);letter-spacing:1px;line-height:1}
.nav{right:60px;top:0;height:84px;display:flex;list-style:none}
.nav li{height:84px;display:flex;align-items:center;padding:0 24px;font-size:15px;letter-spacing:1px;color:var(--green-dark);text-transform:uppercase}
.nav li.active{background:var(--green);color:var(--white)}

/* hero */
.hero{top:84px;left:0;width:1200px;height:552px;background:linear-gradient(120deg,#6e6a63 0%,#b7b3ab 30%,#9aa53c 55%,#c5c9a8 70%,#56565a 100%)}
.hero-card{left:252px;top:75px;width:696px;height:386px;background:rgba(255,255,255,.84);text-align:center}
.anniv{position:absolute;left:298px;top:48px;width:100px;height:100px;border:5px solid var(--green-dark);border-radius:50%;display:flex;align-items:center;justify-content:center;font-size:46px;font-weight:700;color:var(--ink)}
.hero-title{position:absolute;left:0;right:0;top:215px;font-size:34px;font-weight:700;letter-spacing:3px;color:var(--ink)}
.btn{display:inline-flex;align-items:center;justify-content:center;font-size:15px;letter-spacing:.5px}
.btn-pill{position:absolute;left:240px;top:285px;width:216px;height:44px;background:var(--green-dark);color:var(--white);border-radius:22px}

/* values */
.value{width:320px;text-align:center}
.value svg{display:block;margin:0 auto}
.value h3{margin-top:16px;font-size:19px;font-weight:500;color:var(--green-dark);letter-spacing:.5px}
.value p{margin-top:10px;font-size:14px;line-height:24px;color:var(--ink)}

/* approach */
.approach-icon{left:558px;top:1083px;width:84px;height:84px;border-radius:50%;background:radial-gradient(circle at 50% 55%,#e8c9a1 0 22%,#7d4a2f 23% 32%,var(--green) 33%)}
.section-title{left:0;width:1200px;text-align:center;font-size:31px;font-weight:700;letter-spacing:1.5px;color:#333}
.method-lockup{display:flex;align-items:center;gap:30px}
.method-lockup .dot{width:80px;height:80px;border-radius:50%;border:5px solid var(--green)}
.method-lockup span{font-size:34px;font-weight:300;line-height:38px;letter-spacing:1px;text-transform:uppercase}
.lockup-light span{color:#444}
.lockup-dark span{color:var(--white)}
.lockup-dark .dot{border-color:var(--white)}
.method-intro{left:620px;top:1300px;width:446px;text-align:center}
.method-intro h2{font-size:24px;font-weight:500;color:#333}
.method-intro h2 b{color:var(--green-dark);font-weight:700}
.method-intro p{margin-top:10px;font-size:14.5px;line-height:24.5px;color:var(--ink)}

/* steps */
.step{top:1627px;width:310px;height:360px;background:var(--white);border-top:6px solid var(--green);box-shadow:0 2px 10px rgba(0,0,0,.16);text-align:center;padding:30px 22px 0}
.step svg{display:block;margin:0 auto}
.step h3{margin-top:20px;font-size:23px;font-weight:700;letter-spacing:1.5px;color:#222}
.step p{margin-top:8px;font-size:15px;line-height:24.5px;color:var(--ink)}

/* band */
.band{top:2077px;left:0;width:1200px;height:403px;background:var(--green-dark)}
.band-copy{left:653px;top:106px;width:460px;color:var(--white)}
.band-copy h2{font-size:27px;font-weight:500;letter-spacing:.5px}
.band-copy p{margin-top:18px;font-size:14.5px;line-height:25px}
.btn-outline{margin-top:26px;width:168px;height:40px;border:2px solid var(--white);color:var(--white)}

/* heritage */
.heritage{top:2480px;left:0;width:1200px;height:545px;background:linear-gradient(135deg,#2a4e5c 0%,#5f8d9b 35%,#c9d2cf 55%,#4c7886 75%,#1f3f4b 100%)}
.heritage-card{left:239px;top:44px;width:720px;height:436px;background:rgba(255,255,255,.86);border:6px solid var(--green-dark);text-align:center}
.heritage-card h2{margin-top:88px;font-size:31px;font-weight:700;letter-spacing:2px;color:#222}
.heritage-card p{margin-top:30px;font-size:16px;line-height:33px;color:var(--ink)}
.btn-solid{margin-top:26px;width:176px;height:42px;background:var(--green-dark);color:var(--white)}

/* footer */
.site-footer{top:3025px;left:0;width:1200px;height:296px;background:var(--footer);color:#e6e6e6}
.footer-brand{left:93px;top:30px;font-size:40px;font-weight:500;color:var(--white);letter-spacing:1px;line-height:1}
.footer-info{left:93px;top:112px;font-size:13.5px;line-height:22.3px}
.footer-info b{font-weight:700;color:var(--white)}
.copyright{right:89px;top:246px;font-size:13.5px;letter-spacing:.5px}
</style>
</head>
<body>

<header class="site-header abs">
  <div class="brand abs">TARVEK</div>
  <ul class="nav abs">
    <li class="active">Home</li><li>About</li><li>FPM</li><li>Heritage</li><li>Team</li><li>Blog</li><li>Contact</li>
  </ul>
</header>

<section class="hero abs" role="img" aria-label="Photograph of folded knitted sweaters in lime green and grey wool">
  <div class="hero-card abs">
    <div class="anniv">40</div>
    <h1 class="hero-title">TAILORED WEAVING SOLUTIONS</h1>
    <span class="btn btn-pill">Our Approach</span>
  </div>
</section>

<div class="value abs" style="left:88px;top:740px">
  <svg width="80" height="84" viewBox="0 0 80 84" fill="none" stroke="#76ab0a" stroke-width="2.5"><circle cx="40" cy="22" r="8"/><path d="M26 52v-12a14 14 0 0 1 28 0v12"/><rect x="16" y="52" width="48" height="22"/><path d="M8 78h64M40 4v6M28 8l3 5M52 8l-3 5"/></svg>
  <h3>Experience</h3>
  <p>Over the years the company has gained the knowledge and skills that define the superiority of our product and the rigor of our work ethic</p>
</div>
<div class="value abs" style="left:440px;top:740px">
  <svg width="84" height="84" viewBox="0 0 84 84" fill="none" stroke="#76ab0a" stroke-width="2.5"><circle cx="22" cy="58" r="12"/><circle cx="22" cy="58" r="4"/><path d="M54 6a20 20 0 0 1 12 36v10H46V42A20 20 0 0 1 54 6z"/><path d="M48 58h16M50 64h12"/></svg>
  <h3>Creativity</h3>
  <p>Our belief is that the key to our clients' success is a combination of innovation, creativity and quality.<br>We strive to adapt and re-imagine our product</p>
</div>
<div class="value abs" style="left:794px;top:740px">
  <svg width="84" height="84" viewBox="0 0 84 84" fill="none" stroke="#76ab0a" stroke-width="2.5"><circle cx="42" cy="16" r="8"/><circle cx="20" cy="26" r="7"/><circle cx="64" cy="26" r="7"/><path d="M30 78V40a12 12 0 0 1 24 0v38M8 78V46a12 12 0 0 1 16-10M76 78V46a12 12 0 0 0-16-10"/></svg>
  <h3>Professionality</h3>
  <p>We are a family business at the core. Our company is run with the same values as the Varena family: respect, determination and commitment.</p>
</div>

<div class="approach-icon abs" role="img" aria-label="Illustration of a handshake in a green circle"></div>
<h2 class="section-title abs" style="top:1186px">OUR APPROACH</h2>

<div class="method-lockup lockup-light abs" style="left:140px;top:1330px">
  <div class="dot"></div><span>Fluid<br>Partner<br>Method</span>
</div>
<div class="method-intro abs">
  <h2><b>TVKS</b> Fluid Partner Method</h2>
  <p>We believe that the key to delivering a yarn that exceeds our client's expectation is to work together with weavers from step one, starting from the desired end product and working backwards. This allows us to develop the product that our weavers need, rather than having weavers adapt to the supplied raw materials. Our Fluid Partner Method consists achieving maximum flexibility both in development and production.</p>
</div>

<article class="step abs" style="left:91px">
  <svg width="76" height="76" viewBox="0 0 76 76" fill="none" stroke="#8cc21f" stroke-width="2.5"><path d="M38 16a18 18 0 0 1 10 33v9H28v-9a18 18 0 0 1 10-33z"/><path d="M30 64h16M32 70h12M38 2v6M12 12l5 5M64 12l-5 5M4 34h7M72 34h-7"/></svg>
  <h3>IDEATION</h3>
  <p>We define goal and parameters meeting with all the players, designers, technicians, sales force and logistics. We analyse together all aspects and factors: Strategy, technology, raw materials and markets in order to define our GOALS</p>
</article>
<article class="step abs" style="left:445px">
  <svg width="76" height="76" viewBox="0 0 76 76" fill="none" stroke="#8cc21f" stroke-width="2.5"><path d="M68 8C48 8 32 22 26 44l6 6c22-6 36-22 36-42z"/><circle cx="50" cy="26" r="6"/><path d="M26 44l-12-2 10-12h12M32 50l2 12 12-10V40M20 56L8 68"/></svg>
  <h3>EXECUTION</h3>
  <p>One the goals are defined, our FPM team starts staging internal meetings and working with technicians, technical partners, yarn and raw materials supplier, and prodice the forst proto-type for testing and analysing</p>
</article>
<article class="step abs" style="left:799px">
  <svg width="76" height="76" viewBox="0 0 76 76" fill="none" stroke="#8cc21f" stroke-width="2.5"><path d="M6 6l24 24M6 6h14M6 6v14M70 6L46 30M70 6H56M70 6v14M6 70l24-24M6 70h14M6 70V56M70 70L46 46M70 70H56M70 70V56"/></svg>
  <h3>SCALING PRODUCTION</h3>
  <p>When the novelty yarn is defined, the process of scaling upstarts. Putting the value-added product into production at an industrial scale, making sure through continuous tuning thatthe most efficient and successful processes are adopted.</p>
</article>

<section class="band abs">
  <div class="method-lockup lockup-dark abs" style="left:133px;top:130px">
    <div class="dot"></div><span>Fluid<br>Partner<br>Method</span>
  </div>
  <div class="band-copy abs">
    <h2>Production built around you</h2>
    <p>Versatility and flexibility both in development and production are key in delivering a custom solution capable of giving life to your products.</p>
    <span class="btn btn-outline">Find out more</span>
  </div>
</section>

<section class="heritage abs" role="img" aria-label="Close-up photograph of teal blue yarn">
  <div class="heritage-card abs">
    <h2>HERITAGE</h2>
    <p>Our team has decades of experience in providing yarn solutions to weavers<br>around the world, assisting them in the creation of outstanding textiles.<br>Our clients can expect open lines of communication, clarity and professionality</p>
    <span class="btn btn-solid">Check our Heritage</span>
  </div>
</section>

<footer class="site-footer abs">
  <div class="footer-brand abs">TARVEK</div>
  <div class="footer-info abs">
    <b>Corvale S.R.L</b><br>
    Via dei Tessitori 14 59100 Prato - Italy<br>
    Tel. 0574 20418 r.a.<br>
    Fax 0574 20419<br>
    R.E.A PO 481920- Reg. Imp. PO 04718230915<br>
    <b>P. IVA 00482710635</b> - Cod. Fisc. 04718230915<br>
    Capitale sociale € 91. 541, 99 int. ver.
  </div>
  <div class="copyright abs">© COPYRIGHT 2018. ALL RIGHTS RESERVED.</div>
</footer>

</body>
</html>
```